MRHT Needs Fundraiser Dinner Invite!!

The Marisol Hendrick Trust, a 501 3(c) non for profit has a yearly fundraiser, with varying themes. Last year it was "cowboys" and "cowgirls"
This year, it is Club Orchid, or 70's disco music. I have uploaded last years invite for reference, some stock photography for inspiration. You are not limited to using the stock photos.

Annual MRHT Fundraiser Dinner
October 13th, 2022
Starts: 6:30pm
RSVP By: September 20th
Place: The Bramwell
Price: $135 per ticket

Target Market(s)

Donors, Business People, Every person

Industry/Entity Type

Non for Profit

Font styles to use
Sans Serif

Colors
0054AA
0677BA
7BADD7
CADEEF
E8F1F8
E54698
E96AAD
F1A4CE
F9D9EA
FCEFF6
6B429C
8869AF
B7A5CE
E3DAEB
F3F0F8

Requirements
Must have
• The invite should be 5x7, be sophisticated as the clientele are mainly business people that come to support the cause. It should be fun and inviting at the same time.

```html
<!DOCTYPE html>
<html lang="en">
<head>
<meta charset="UTF-8">
<title>MRHT Fundraiser Dinner Invite</title>
<link rel="stylesheet" href="https://fonts.googleapis.com/css2?family=Baloo+2:wght@700;800&family=Exo+2:wght@500;600;700;800&display=swap">
<style>
  :root {
    --page: #ffffff;
    --sun: #ffd400;
    --sun-light: #fff200;
    --tangerine: #f7931e;
    --magenta: #e23fd6;
    --magenta-deep: #a02bb0;
    --violet: #5a2be0;
    --violet-soft: #8a5ae8;
    --sky: #2a8cf0;
    --ink: #111111;
    --white: #ffffff;
  }
  html, body {
    margin: 0;
    width: 1200px;
    height: 1000px;
    overflow: hidden;
    background: var(--page);
  }
  .invite {
    position: absolute;
    left: 283px;
    top: 56px;
    width: 634px;
    height: 887px;
  }
  .invite svg { display: block; width: 100%; height: 100%; }
  .display { font-family: "Baloo 2", "Arial Rounded MT Bold", sans-serif; font-weight: 800; }
  .body-type { font-family: "Exo 2", "Arial", sans-serif; }
  .tagline { fill: var(--violet); font-size: 40px; }
  .numeral { fill: var(--magenta); stroke: #f6c8f0; stroke-width: 5; paint-order: stroke; }
  .numeral-shadow { fill: var(--magenta-deep); }
  .headline { fill: var(--white); stroke: var(--ink); stroke-width: 12; paint-order: stroke; stroke-linejoin: round; font-size: 84px; }
  .event-date { fill: var(--magenta-deep); font-weight: 700; font-size: 58px; }
  .event-year { fill: var(--violet); font-weight: 700; font-size: 28px; letter-spacing: 14px; }
  .kicker { fill: var(--violet); font-weight: 700; font-size: 18px; }
  .org-name { fill: var(--violet); font-weight: 800; font-size: 112px; }
  .org-full { fill: var(--violet); font-weight: 500; font-size: 13.5px; }
  .org-event { fill: var(--violet); font-weight: 700; font-size: 20px; letter-spacing: 3px; }
  .detail { fill: var(--white); font-weight: 700; }
  .rsvp { fill: var(--magenta-deep); font-weight: 600; font-size: 21px; }
  .rsvp-date { fill: var(--violet); }
  .arrows-left { fill: var(--magenta); }
  .arrows-right { fill: var(--violet); }
</style>
</head>
<body>
<main class="invite">
  <svg viewBox="0 0 750 1050" xmlns="http://www.w3.org/2000/svg">
    <defs>
      <linearGradient id="dancer-tone" x1="0" y1="0" x2="1" y2="0.2">
        <stop offset="0" stop-color="#ffd400"/>
        <stop offset="0.45" stop-color="#ffc21a"/>
        <stop offset="0.7" stop-color="#f7931e"/>
        <stop offset="1" stop-color="#f7a21e"/>
      </linearGradient>
    </defs>

    <rect class="backdrop" width="750" height="1050" fill="var(--sun)"/>
    <rect class="dancer-art" width="750" height="1050" fill="url(#dancer-tone)" role="img"
          aria-label="Illustration of a disco dancer silhouette in orange, arm raised, among soft yellow light circles"/>

    <g transform="rotate(-8 260 110)">
      <text class="display tagline" x="58" y="140">c’mon, it’s time for</text>
    </g>

    <g class="display" transform="rotate(-3 330 330)">
      <text class="numeral-shadow" x="52" y="508" font-size="400">70</text>
      <text class="numeral" x="66" y="494" font-size="400">70</text>
      <text class="numeral-shadow" x="528" y="262" font-size="150">’s</text>
      <text class="numeral" x="538" y="252" font-size="150">’s</text>
    </g>

    <g class="headline-band">
      <polygon points="72,560 700,460 700,570 72,670" fill="var(--magenta)"/>
      <polygon points="86,524 711,424 711,534 86,634" fill="var(--violet)"/>
      <g transform="rotate(-9 395 540)">
        <text class="display headline" x="395" y="572" text-anchor="middle">DiSCO MUSiC</text>
      </g>
    </g>

    <g class="body-type" transform="rotate(-5 530 650)">
      <text class="event-date" x="528" y="672" text-anchor="middle">13/10</text>
      <text class="event-year" x="536" y="700" text-anchor="middle">2022</text>
    </g>

    <g class="body-type">
      <text class="kicker" x="62" y="741">GET GROOVY FOR OUR ANNUAL</text>
      <text class="org-name" x="217" y="840" text-anchor="middle">MRHT</text>
      <text class="org-full" x="212" y="862" text-anchor="middle">THE MARISOL HENDRICK TRUST</text>
      <text class="org-event" x="212" y="889" text-anchor="middle">FUNDRAISER DINNER</text>
    </g>

    <g class="body-type details">
      <polygon points="412,760 750,725 750,757 412,792" fill="var(--magenta)"/>
      <text class="detail" x="432" y="783" font-size="24" transform="rotate(-6 432 783)">AT <tspan font-size="30">THE BRAMWELL</tspan></text>

      <polygon points="412,812 745,775 745,805 412,842" fill="var(--violet-soft)"/>
      <text class="detail" x="432" y="835" font-size="18" transform="rotate(-6 432 835)">MUSIC START AT <tspan font-size="24">6:30 PM</tspan></text>

      <polygon points="412,866 750,822 750,876 412,920" fill="var(--sky)"/>
      <text class="detail" x="432" y="905" font-size="28" transform="rotate(-7 432 905)">TICKET <tspan font-size="40">$135</tspan></text>
    </g>

    <g class="body-type rsvp-line">
      <g class="arrows-left">
        <polygon points="0,973 12,981 0,989"/><polygon points="13,973 25,981 13,989"/>
        <polygon points="26,973 38,981 26,989"/><polygon points="39,973 51,981 39,989"/>
        <polygon points="52,973 64,981 52,989"/><polygon points="65,973 77,981 65,989"/>
        <polygon points="78,973 90,981 78,989"/><polygon points="91,973 103,981 91,989"/>
      </g>
      <text class="rsvp" x="106" y="988">let us know if you will come by <tspan class="rsvp-date">20/09/2022</tspan></text>
      <g class="arrows-right">
        <polygon points="667,981 679,973 679,989"/><polygon points="680,981 692,973 692,989"/>
        <polygon points="693,981 705,973 705,989"/><polygon points="706,981 718,973 718,989"/>
        <polygon points="719,981 731,973 731,989"/><polygon points="732,981 744,973 744,989"/>
      </g>
    </g>
  </svg>
</main>
</body>
</html>
```